Business Cards for cafe providing speciality coffee and food

I need a business card design for my husband’s businesses. He has two cafes in Brisbane. The business name is Copperleaf Roasting House. They sell high end specialty coffee as well as breakfast and lunch. All the food is cooked fresh, in house and they have strict quality controls for their coffee. I would like the business card to feature the address for both cafes, my husband’s phone number and the business’s instagram. The address for the first is 61 Walden Crescent, Oakvale and the second is 23 Pellow Avenue, Brindlemoor. The Instagram handle is @copperleafroastinghouse and phone number is 0491362847. We already have a business logo that is attached.

Target Market(s)

All ages, higher disposable income and more likely to eat out regularly

Industry/Entity Type

Hospitality

Contact Information for Business Card

Must be suitable for both customers and suppliers

Font styles to use
Sans Serif

Colors

Designer to choose colors to be used in the design.

Requirements
Must have
• Owner’s name: Reid Castell
• Addresses of both cafes: 61 Walden Crescent, Oakvale and 23 Pellow Avenue, Brindlemoor
• Instagram handle: @copperleafroastinghouse
• Contact number: 0491362847
Nice to have
• Business logo

```html
<!DOCTYPE html>
<html lang="en">
<head>
<meta charset="utf-8">
<title>Copperleaf Roasting House – Business Card</title>
<link rel="stylesheet" href="https://fonts.googleapis.com/css2?family=Work+Sans:wght@400;500;700&display=swap">
<style>
  :root {
    --backdrop: #e9e6e1;
    --card: #ffffff;
    --ink: #1e1e1e;
    --ink-soft: #3a3a3a;
    --pattern-light: #f4f4f4;
    --pattern-mid: #e4e4e4;
    --shadow: rgba(0, 0, 0, 0.18);
  }
  * { box-sizing: border-box; margin: 0; padding: 0; }
  html, body { width: 1200px; height: 1040px; overflow: hidden; }
  body {
    background: var(--backdrop);
    font-family: "Work Sans", Arial, sans-serif;
    color: var(--ink);
    position: relative;
  }
  .card {
    position: absolute;
    top: 180px;
    width: 400px;
    height: 680px;
    background: var(--card);
    box-shadow: 0 10px 30px var(--shadow);
  }
  .card--front { left: 150px; }
  .card--back { left: 650px; overflow: hidden; }

  .brand-mark {
    position: absolute;
    top: 70px;
    right: 40px;
    width: 170px;
    text-align: center;
  }
  .brand-mark__circle {
    width: 84px;
    height: 84px;
    border-radius: 50%;
    background: var(--ink);
    margin: 0 auto 14px;
  }
  .brand-mark__name {
    font-weight: 700;
    font-size: 15px;
    letter-spacing: 2px;
    text-transform: uppercase;
    line-height: 1.4;
    color: var(--ink);
  }

  .contact {
    position: absolute;
    left: 40px;
    top: 370px;
    right: 30px;
  }
  .contact__name {
    font-weight: 700;
    font-size: 27px;
    letter-spacing: 0.5px;
    text-transform: uppercase;
  }
  .contact__wave { display: block; margin: 14px 0 18px; }
  .contact__address {
    font-size: 17px;
    line-height: 1.3;
    color: var(--ink-soft);
    font-style: normal;
  }
  .contact__row {
    display: flex;
    align-items: center;
    gap: 10px;
    font-size: 17px;
    color: var(--ink-soft);
    margin-top: 4px;
  }
  .contact__row:first-of-type { margin-top: 8px; }
  .contact__icon { width: 16px; height: 16px; flex: none; }
  .contact__dot {
    width: 12px; height: 12px; margin: 0 2px;
    border-radius: 50%; background: var(--ink); flex: none;
  }

  .back-pattern {
    position: absolute;
    inset: 0;
    background: radial-gradient(circle at 50% 50%, var(--pattern-light), var(--pattern-mid));
  }
  .back-brand {
    position: absolute;
    top: 36px;
    right: 30px;
    font-weight: 700;
    font-size: 10px;
    letter-spacing: 1.5px;
    text-transform: uppercase;
    color: var(--ink);
    text-align: right;
    line-height: 1.4;
  }
</style>
</head>
<body>

  <section class="card card--front" aria-label="Business card front">
    <div class="brand-mark">
      <div class="brand-mark__circle"></div>
      <p class="brand-mark__name">Copperleaf<br>Roasting House</p>
    </div>

    <div class="contact">
      <h1 class="contact__name">Reid Castell</h1>
      <svg class="contact__wave" width="40" height="8" viewBox="0 0 40 8" aria-hidden="true">
        <path d="M1 4 Q6 0 11 4 T21 4 T31 4 T39 4" fill="none" stroke="#1e1e1e" stroke-width="2"/>
      </svg>
      <address class="contact__address">
        61 Walden Crescent<br>
        Oakvale and 23 Pellow Avenue<br>
        Brindlemoor
      </address>
      <p class="contact__row">
        <svg class="contact__icon" viewBox="0 0 24 24" aria-hidden="true">
          <path d="M6.6 10.8a15.1 15.1 0 0 0 6.6 6.6l2.2-2.2a1 1 0 0 1 1-.25 11.4 11.4 0 0 0 3.6.57 1 1 0 0 1 1 1V20a1 1 0 0 1-1 1A17 17 0 0 1 3 4a1 1 0 0 1 1-1h3.5a1 1 0 0 1 1 1c0 1.25.2 2.45.57 3.6a1 1 0 0 1-.25 1z" fill="#1e1e1e"/>
        </svg>
        0491362847
      </p>
      <p class="contact__row">
        <span class="contact__dot" aria-hidden="true"></span>
        @copperleafroastinghouse
      </p>
    </div>
  </section>

  <section class="card card--back" aria-label="Business card back">
    <div class="back-pattern" role="img" aria-label="Faint repeating pattern of the brand emblem across the card"></div>
    <p class="back-brand">Copperleaf<br>Roasting House</p>
  </section>

</body>
</html>
```